Accounting and Financial Services Firm - Modern, Fresh, Original, Professional

We need a business card designed. We would like to see use of the the colors blue. Logo attached.

Modern, Fresh, Original, Professional,
Updates

Email section on business card required. design brief updated.

Target Market(s)

Small to medium businesses and high net worth individuals

Industry/Entity Type

Public Accounting

Contact Information for Business Card

Business Name: PM Ledgerline Chartered Accountants
Address: Level 14, 82 Harrow Lane Sydney NSW 2000
Ph: 02 9314 2587
Mobile: 04 XXXX XXXX
Email: anna@pmledgerline.com.au
Wechat ID: XXXXXXX
Website: www.pmledgerline.com.au

Name: Anna Petrov
Position: Manager

Font styles to use
Sans Serif

Colors
0492cd
33a6d7
85cae6

Requirements
Must have
• Modern font.

```html
<!DOCTYPE html>
<html lang="en">
<head>
<meta charset="utf-8">
<title>PM Ledgerline Chartered Accountants – Business Card</title>
<link rel="stylesheet" href="https://fonts.googleapis.com/css2?family=Montserrat:wght@400;500;600;700&display=swap">
<style>
  :root {
    --blue: #0492cd;
    --blue-mid: #33a6d7;
    --blue-light: #85cae6;
    --ink: #231f20;
    --grey-text: #58595b;
    --grey-band: #c9cacc;
    --paper: #ffffff;
    --stage: #2b2e32;
  }
  * { box-sizing: border-box; margin: 0; padding: 0; }
  html, body {
    width: 1200px; height: 900px; overflow: hidden;
    background: var(--stage);
    font-family: "Montserrat", Arial, sans-serif;
  }
  .sheet {
    width: 1200px; height: 900px;
    display: flex; align-items: center; justify-content: center; gap: 60px;
  }
  .card {
    position: relative;
    width: 520px; height: 300px;
    border-radius: 22px;
    overflow: hidden;
  }
  .card-bands { position: absolute; inset: 0; width: 100%; height: 100%; }

  /* Front */
  .card-front { background: var(--paper); }
  .contact-block { position: absolute; left: 34px; top: 28px; color: var(--grey-text); }
  .person-name {
    font-size: 22px; font-weight: 700; color: var(--blue);
    text-transform: uppercase; letter-spacing: 0.5px; line-height: 1;
  }
  .person-role { font-size: 14px; font-weight: 500; margin-top: 3px; }
  .contact-list { list-style: none; margin-top: 14px; }
  .contact-item {
    display: flex; align-items: center; gap: 8px;
    font-size: 13.5px; font-weight: 500; line-height: 1; margin-bottom: 6px;
  }
  .contact-icon { width: 14px; height: 14px; flex: none; }
  .address { margin-top: 12px; font-size: 13.5px; font-weight: 500; line-height: 1.35; }
  .front-brand {
    position: absolute; right: 72px; top: 130px;
    font-size: 15px; font-weight: 600; color: var(--blue);
    letter-spacing: 1px; text-transform: uppercase;
  }
  .website {
    position: absolute; left: 210px; bottom: 24px;
    font-size: 16px; font-weight: 600; color: var(--blue);
  }

  /* Back */
  .card-back { background: var(--ink); }
  .back-brand {
    position: absolute; inset: 0;
    display: flex; flex-direction: column; align-items: center; justify-content: center;
    color: var(--blue); font-weight: 500; text-transform: uppercase;
  }
  .brand-name { font-size: 40px; letter-spacing: 1px; line-height: 1; }
  .brand-tagline { font-size: 13px; letter-spacing: 3.4px; margin-top: 8px; }
</style>
</head>
<body>
<main class="sheet">

  <section class="card card-front" aria-label="Business card front">
    <svg class="card-bands" viewBox="0 0 520 300" aria-hidden="true">
      <polygon points="430,0 520,0 520,300 500,300" fill="var(--blue-light)"/>
      <polygon points="392,232 520,232 520,300 400,300" fill="var(--grey-band)" opacity="0.55"/>
    </svg>
    <div class="contact-block">
      <h1 class="person-name">Anna Petrov</h1>
      <p class="person-role">Manager</p>
      <ul class="contact-list">
        <li class="contact-item">
          <svg class="contact-icon" viewBox="0 0 14 14"><circle cx="7" cy="7" r="7" fill="var(--blue)"/><rect x="4.5" y="3" width="5" height="8" rx="1" fill="none" stroke="#fff" stroke-width="1.2"/></svg>
          02 9314 2587
        </li>
        <li class="contact-item">
          <svg class="contact-icon" viewBox="0 0 14 14"><circle cx="7" cy="7" r="7" fill="var(--blue)"/><path d="M4.6 3.6l1.4-.3.8 1.8-.9.7a4.5 4.5 0 0 0 2.3 2.3l.7-.9 1.8.8-.3 1.4C8 9.6 4.4 6 4.6 3.6z" fill="#fff"/></svg>
          04 XXXX XXXX
        </li>
        <li class="contact-item">
          <svg class="contact-icon" viewBox="0 0 14 14"><circle cx="7" cy="7" r="7" fill="var(--blue)"/><rect x="3.5" y="4.5" width="7" height="5" rx="0.6" fill="#fff"/><path d="M3.8 4.9L7 7.3l3.2-2.4" fill="none" stroke="var(--blue)" stroke-width="0.9"/></svg>
          anna@pmledgerline.com.au
        </li>
        <li class="contact-item">
          <svg class="contact-icon" viewBox="0 0 14 14"><circle cx="7" cy="7" r="7" fill="var(--blue)"/><ellipse cx="7" cy="6.6" rx="3.4" ry="2.6" fill="#fff"/><path d="M5 8.4l-.6 1.8 2-1.2z" fill="#fff"/></svg>
          Wechat ID: XXXXXXX
        </li>
      </ul>
      <p class="address">Level 14, 82 Harrow Lane<br>Sydney NSW 2000</p>
    </div>
    <p class="front-brand">PM Ledgerline</p>
    <p class="website">www.pmledgerline.com.au</p>
  </section>

  <section class="card card-back" aria-label="Business card back">
    <svg class="card-bands" viewBox="0 0 520 300" aria-hidden="true">
      <polygon points="0,0 300,0 0,150" fill="var(--blue-light)"/>
      <polygon points="520,130 520,300 250,300" fill="var(--grey-band)"/>
    </svg>
    <div class="back-brand">
      <p class="brand-name">PM Ledgerline</p>
      <p class="brand-tagline">Chartered Accountants</p>
    </div>
  </section>

</main>
</body>
</html>
```